Brand New Upscale OOBGYN Office

Im in Need of an advertising one sided postcard as soon as possible. It's for a brand new OBGYN office in the Northern Virginia area. We are trying to create a new patient customer base. I have attached photos of the inside of the office and logos. The office contact information needs to be on the postcard. You can find that on the attached pdf file named business card. That same file is the font that needs to be used. The font is called TT Drugs. Please contact me with any questions. I would appreciated it so much if you could send me these proofs as soon as possible. Thank you!!!
Women
Advertising
- TT Drugs

```html
<!DOCTYPE html>
<html lang="en">
<head>
<meta charset="utf-8">
<title>Laurel Ridge OBGYN – Postcard</title>
<link rel="stylesheet" href="https://fonts.googleapis.com/css2?family=Raleway:wght@300;400;500&display=swap">
<style>
  :root {
    --page-bg: #ecebe8;
    --card-dark: #38383a;
    --mint: #aedcc6;
    --badge-grey: #6e6e71;
    --brand-grey: #8c8c8f;
    --band-overlay: rgba(112, 96, 94, 0.62);
    --text-light: #ffffff;
    --photo-light: #d2ab9b;
    --photo-mid: #8d6b5f;
    --photo-deep: #3b2b27;
  }
  * { margin: 0; padding: 0; box-sizing: border-box; }
  html, body {
    width: 1200px; height: 900px; overflow: hidden;
    background: var(--page-bg);
    font-family: "Raleway", "Helvetica Neue", Arial, sans-serif;
  }
  .postcard {
    position: absolute; left: 100px; top: 58px;
    width: 1000px; height: 783px; overflow: hidden;
    background: var(--card-dark);
    box-shadow: 0 6px 24px rgba(0,0,0,0.18);
  }
  .hero-photo {
    position: absolute; inset: 0 0 160px 0;
    background:
      radial-gradient(ellipse 30% 35% at 42% 55%, var(--photo-light), transparent 70%),
      radial-gradient(ellipse 28% 30% at 80% 38%, #b68d7e, transparent 70%),
      linear-gradient(160deg, #a88273 0%, var(--photo-mid) 45%, var(--photo-deep) 100%);
  }
  .card-shapes { position: absolute; inset: 0; width: 1000px; height: 783px; }
  .headline-band {
    position: absolute; left: 0; top: 0; width: 1000px; height: 130px;
    background: var(--band-overlay);
  }
  .headline {
    position: absolute; left: 40px; top: 30px; width: 490px;
    color: var(--text-light); font-weight: 400; font-size: 26px;
    line-height: 31px; letter-spacing: 1.5px; text-transform: uppercase;
  }
  .band-divider {
    position: absolute; left: 571px; top: 30px; width: 2px; height: 84px;
    background: rgba(255,255,255,0.8);
  }
  .consult {
    position: absolute; right: 22px; top: 30px; text-align: right;
    color: var(--text-light);
  }
  .consult-title { font-size: 25px; letter-spacing: 1.5px; text-transform: uppercase; line-height: 30px; }
  .consult-phone { font-size: 31px; letter-spacing: 1px; line-height: 40px; margin-top: 4px; }
  .consult-web { font-size: 20px; line-height: 26px; margin-top: 2px; }
  .consult svg { vertical-align: -3px; margin-right: 6px; fill: var(--text-light); }
  .brand-badge {
    position: absolute; left: 87px; top: 347px; width: 230px; height: 230px;
    border-radius: 50%; background: var(--badge-grey);
  }
  .brand-name {
    position: absolute; left: 31px; top: 630px;
    color: var(--brand-grey); font-weight: 300; font-size: 30px;
    letter-spacing: 1px; text-transform: uppercase; white-space: nowrap;
  }
  .brand-rule {
    position: absolute; left: 31px; top: 673px; width: 340px; height: 1px;
    background: var(--brand-grey);
  }
  .brand-tagline {
    position: absolute; left: 31px; top: 681px;
    color: var(--brand-grey); font-weight: 300; font-size: 21px; letter-spacing: 4px;
  }
  .contact-divider {
    position: absolute; left: 394px; top: 615px; width: 2px; height: 130px;
    background: rgba(255,255,255,0.85);
  }
  .contact-list {
    position: absolute; left: 412px; top: 620px; list-style: none;
    color: var(--text-light); font-size: 19px; line-height: 26px;
  }
  .contact-list li { display: flex; align-items: flex-start; gap: 10px; margin-bottom: 1px; }
  .contact-list svg { flex: none; fill: var(--text-light); margin-top: 4px; }
  .contact-list .address { line-height: 25px; margin-bottom: 6px; }
</style>
</head>
<body>
  <article class="postcard">
    <div class="hero-photo" role="img" aria-label="Photo of a mother resting beside her sleeping newborn baby, in soft warm tones"></div>

    <svg class="card-shapes" viewBox="0 0 1000 783" aria-hidden="true">
      <path d="M0,300 C200,390 380,500 560,545 C760,590 920,572 1000,560 L1000,783 L0,783 Z" fill="var(--mint)"/>
      <path d="M0,316 C200,410 380,520 560,560 C760,603 920,592 1000,590 L1000,783 L0,783 Z" fill="var(--card-dark)"/>
      <rect x="0" y="755" width="1000" height="28" fill="var(--mint)"/>
    </svg>

    <div class="headline-band"></div>
    <h1 class="headline">Laurel Ridge OBGYN is Northern Virginia's premiere womens health center.</h1>
    <div class="band-divider"></div>
    <div class="consult">
      <p class="consult-title">Schedule a consultation:</p>
      <p class="consult-phone"><svg width="22" height="24" viewBox="0 0 24 24"><path d="M6.6 10.8a15.1 15.1 0 0 0 6.6 6.6l2.2-2.2c.3-.3.7-.4 1-.2 1.1.4 2.3.6 3.6.6.6 0 1 .4 1 1V20c0 .6-.4 1-1 1A17 17 0 0 1 3 4c0-.6.4-1 1-1h3.5c.6 0 1 .4 1 1 0 1.3.2 2.5.6 3.6.1.3 0 .7-.2 1z"/></svg>555-014-2286</p>
      <p class="consult-web"><svg width="18" height="18" viewBox="0 0 24 24"><path d="M12 2a10 10 0 1 0 0 20 10 10 0 0 0 0-20zm6.9 6h-3a15.7 15.7 0 0 0-1.4-3.6A8 8 0 0 1 18.9 8zM12 4c.8 1.2 1.5 2.5 1.9 4h-3.8c.4-1.5 1.1-2.8 1.9-4zM4.3 14a8 8 0 0 1 0-4h3.4a16 16 0 0 0 0 4zm.8 2h3a15.7 15.7 0 0 0 1.4 3.6A8 8 0 0 1 5.1 16zm3-8h-3a8 8 0 0 1 4.4-3.6C8.9 5.5 8.4 6.7 8.1 8zM12 20c-.8-1.2-1.5-2.5-1.9-4h3.8c-.4 1.5-1.1 2.8-1.9 4zm2.3-6H9.7a14.7 14.7 0 0 1 0-4h4.6a14.7 14.7 0 0 1 0 4zm.2 5.6c.6-1.1 1.1-2.3 1.4-3.6h3a8 8 0 0 1-4.4 3.6zm1.8-5.6a16 16 0 0 0 0-4h3.4a8 8 0 0 1 0 4z"/></svg>LaurelRidgeOBGYN.com</p>
    </div>

    <div class="brand-badge" aria-hidden="true"></div>
    <p class="brand-name">Laurel Ridge OBGYN</p>
    <div class="brand-rule"></div>
    <p class="brand-tagline">physicians &amp; midwives</p>

    <div class="contact-divider"></div>
    <ul class="contact-list">
      <li class="address">
        <svg width="18" height="24" viewBox="0 0 18 24"><path d="M9 0a9 9 0 0 0-9 9c0 6.8 9 15 9 15s9-8.2 9-15a9 9 0 0 0-9-9zm0 12.5A3.5 3.5 0 1 1 9 5.5a3.5 3.5 0 0 1 0 7z"/></svg>
        <span>Laurel Ridge OBGYN<br>4471 Brookfield Lane, Suite 120 Fairview, VA 20150</span>
      </li>
      <li><svg width="18" height="18" viewBox="0 0 24 24"><rect x="2" y="2" width="20" height="20" rx="3"/><path fill="var(--card-dark)" d="M8.5 11.2a9 9 0 0 0 4.3 4.3l1.4-1.4c.2-.2.5-.3.7-.1.7.2 1.5.4 2.3.4.4 0 .6.3.6.6v2.2c0 .4-.3.6-.6.6A10.8 10.8 0 0 1 6.4 7c0-.4.3-.6.6-.6h2.2c.4 0 .6.3.6.6 0 .8.1 1.6.4 2.3 0 .2 0 .5-.2.7z"/></svg><span>555-014-2286</span></li>
      <li><svg width="20" height="18" viewBox="0 0 24 22"><rect x="6" y="0" width="12" height="6"/><rect x="0" y="7" width="24" height="10" rx="2"/><rect x="5" y="13" width="14" height="9" stroke="var(--card-dark)" stroke-width="1.5"/></svg><span>555-014-7730</span></li>
      <li><svg width="20" height="16" viewBox="0 0 24 16"><rect x="0" y="0" width="24" height="16" rx="1.5"/><path d="M1 1.5l11 8 11-8" fill="none" stroke="var(--card-dark)" stroke-width="1.8"/></svg><span>info@laurelridgeobgyn.com</span></li>
    </ul>
  </article>
</body>
</html>
```